Pest control srevice Special offer

Pest control to promote our service program. 3 month pest control service for $125.00 Includes svc for ants,bees,wasps,silverfish,rats,mice,roaches. No long term contracts Our customers can purchase the service 3 months at a time as needed throughout the year. Or sign up for the full year at 425.00

Target Market(s)

Home Owners

Industry/Entity Type

Pest Control

Font styles to use
Sans Serif

Requirements
Must have
• must be relevant to pest control see our web site at harlowbugandrodentguard.com
Nice to have
• I want the post card to be laid out in a way that describes our service simple and professional. The program that we are offering really works well for our customers and makes sense they only pay for service when they are having an issue
Should not have
• I don't want pictures of insects that scare people off or unsettling to look at

```html
<!DOCTYPE html>
<html lang="en">
<head>
<meta charset="utf-8">
<title>Harlow Bug &amp; Rodent Guard — Service Offer Postcard</title>
<link rel="stylesheet" href="https://fonts.googleapis.com/css2?family=Oswald:wght@300;400;500;600;700&display=swap">
<style>
  :root {
    --sun: #ffcc00;
    --ink: #0c0f1e;
    --paper: #ffffff;
    --alert: #ee1111;
    --trail: #1a1a1a;
  }
  html, body {
    margin: 0;
    padding: 0;
    width: 1200px;
    height: 784px;
    overflow: hidden;
    background: var(--sun);
  }
  .postcard {
    position: relative;
    width: 1200px;
    height: 784px;
    background: var(--sun);
    overflow: hidden;
    font-family: "Oswald", "Arial Narrow", sans-serif;
    text-transform: uppercase;
  }
  .brand {
    position: absolute;
    left: 84px;
    top: 104px;
    width: 180px;
    color: var(--ink);
    font-weight: 600;
    font-size: 30px;
    line-height: 1.05;
    text-align: center;
  }
  .brand .brand-sub {
    display: block;
    font-size: 30px;
  }
  .brand .brand-square {
    display: block;
    width: 14px;
    height: 14px;
    margin: 0 auto 8px;
    background: var(--ink);
  }
  .slash, .pest-trail {
    position: absolute;
    left: 0;
    top: 0;
  }
  .cta {
    position: absolute;
    left: 124px;
    top: 508px;
    width: 372px;
    text-align: right;
  }
  .cta-line {
    display: block;
    color: var(--ink);
    font-weight: 400;
    font-size: 33px;
    line-height: 1.1;
    letter-spacing: 0.5px;
  }
  .cta-phone {
    display: block;
    color: var(--alert);
    font-weight: 600;
    font-size: 62px;
    line-height: 1.05;
    letter-spacing: 1px;
  }
  .offer-panel {
    position: absolute;
    left: 706px;
    top: 56px;
    width: 494px;
    height: 648px;
    background: var(--ink);
    color: var(--paper);
  }
  .offer-panel p { margin: 0; position: absolute; left: 43px; white-space: nowrap; }
  .price { color: var(--sun); }
  .plan-term { top: 88px; font-weight: 700; font-size: 64px; line-height: 1; letter-spacing: 1px; }
  .plan-name { top: 148px; font-weight: 400; font-size: 35px; line-height: 1; letter-spacing: 0.5px; }
  .plan-price { top: 189px; font-weight: 700; font-size: 62px; line-height: 1; letter-spacing: 1px; }
  .plan-includes { top: 256px; font-weight: 400; font-size: 27px; line-height: 35px; letter-spacing: 0.5px; }
  .plan-or {
    top: 372px;
    font-weight: 400;
    font-size: 66px;
    line-height: 1;
    color: transparent;
    -webkit-text-stroke: 2px var(--paper);
  }
  .year-name { top: 456px; font-weight: 400; font-size: 37px; line-height: 1; letter-spacing: 0.5px; }
  .year-price { top: 495px; font-weight: 700; font-size: 62px; line-height: 1; letter-spacing: 1px; }
</style>
</head>
<body>
<main class="postcard">
  <div class="brand">
    <span class="brand-square"></span>
    Harlow Bug
    <span class="brand-sub">&amp; Rodent Guard</span>
  </div>

  <svg class="slash" width="1200" height="784" aria-hidden="true">
    <line x1="118" y1="348" x2="446" y2="79" stroke="var(--alert)" stroke-width="3"/>
  </svg>

  <svg class="pest-trail" width="1200" height="784" role="img" aria-label="Trail of small black ants marching from the slash line down toward the offer panel">
    <path d="M250 250 C330 170 440 170 540 200 C600 300 690 360 706 420 L706 784 L600 784 C590 650 560 560 520 480 C430 420 330 380 250 330 Z"
          fill="var(--trail)" opacity="0.14"/>
  </svg>

  <div class="cta">
    <span class="cta-line">Call for a free estimate!</span>
    <span class="cta-phone">800-555-0142</span>
  </div>

  <section class="offer-panel">
    <p class="plan-term">3 Month</p>
    <p class="plan-name">Pest Control Service</p>
    <p class="plan-price">For <span class="price">$125.00</span></p>
    <p class="plan-includes">Includes svc for<br>Ants, bees, wasps, silverfish,<br>rats, mice, roaches.</p>
    <p class="plan-or">Or</p>
    <p class="year-name">Sign up for the full year</p>
    <p class="year-price">At <span class="price">$425.00</span></p>
  </section>
</main>
</body>
</html>
```